依頼詳細
■ 商品情報:
ギターケーブル

■ 参考URL:http://k8r2.net/QmWe
他社のギターケーブルです。商品のイメージを掴むためにご確認ください。

■ ターゲット:20〜30代のギターを弾く方(男女ともに使えるデザイン)

■ブランド名:VELTOKA
楽器小物を中心に複数商品展開しております。
これまでもクールなパッケージを心がけており、黒、グレー、白はよく使う色です。

■希望デザインイメージ:
・白、グレーベースで使う色は2、3色程度
・VELTOKAのロゴを使用
・洗練されたデザイン
・理想はミレクのようにシンプルなもの
・MORVANEという会社のパッケージが理想なので参考までに載せておきます。

※キャッチコピー等は特に必要ありません。
VELTOKAロゴさえ入れて頂ければ、あとは自由です。
洗練された雰囲気にするため、英語文字が入ってればより良いです。

■ パッケージサイズ
23.3*9.6*2.8cm

展開図がありませんので、お任せ致します。

■ 納品ファイルの希望
AIデータ、PDF

■添付画像一覧
・自社商品
・VELTOKAロゴ
・MORVANEパッケージ
記載項目
種類:紙パッケージ
提案時は立体図ももらえると見やすいので助かります。

表面のデザイン重視
裏面は採用された方に文言、JANコード等をお送りするためそれを貼り付ける程度の簡素なデザインで構いません。
希望イメージ
シンプル 複雑
単色 カラフル
暗い 明るい
日常 高級
遊び心 厳粛
未来的 伝統的
女性的 男性的
希望する色
納品ファイル
• 高解像度JPG (.jpg)
• イラストレーター形式 (.ai)
補足説明
■ 選んだ理由

弊社スタッフで人気投票した結果、一番人気でした。
黒のパッケージが高級感があり、手に取ったときに一番テンションが上がるものだと思ったためです。

■ 提案者全員のお礼・コメント

たくさんのご応募ありがとうございました。
数多くのご応募があり、非常に迷いました。
また機会がありましたらよろしくお願い致します。

```html
<!DOCTYPE html>
<html lang="en">
<head>
<meta charset="utf-8">
<title>VELTOKA Instrument Cable Package</title>
<link rel="stylesheet" href="https://fonts.googleapis.com/css2?family=Cinzel:wght@500&family=Raleway:wght@200;300&display=swap">
<style>
  :root {
    --paper: #ffffff;
    --ink: #2b2b2b;
    --frame: #a8a8a8;
    --soft-grey: #8a8a8a;
    --outline-grey: #b5b5b5;
    --cable-dark: #161616;
    --metal-light: #c9c9c9;
    --metal-mid: #7a7a7a;
  }
  html, body {
    margin: 0;
    padding: 0;
    width: 1200px;
    height: 2324px;
    overflow: hidden;
    background: var(--paper);
  }
  .package-front {
    position: relative;
    width: 1200px;
    height: 2324px;
    background: var(--paper);
  }
  .package-frame {
    position: absolute;
    left: 62px;
    top: 56px;
    width: 1080px;
    height: 2232px;
    border: 3px solid var(--frame);
    box-sizing: border-box;
  }
  .brand-name {
    position: absolute;
    left: 220px;
    top: 160px;
    margin: 0;
    font-family: "Cinzel", serif;
    font-weight: 500;
    font-size: 46px;
    letter-spacing: 2px;
    color: var(--ink);
    line-height: 1;
  }
  .artwork {
    position: absolute;
    left: 0;
    top: 0;
    width: 1200px;
    height: 2324px;
  }
  .headline-word {
    font-family: "Raleway", sans-serif;
    font-weight: 200;
    font-size: 600px;
    fill: none;
    stroke: var(--outline-grey);
    stroke-width: 3;
  }
  .product-type {
    font-family: "Raleway", sans-serif;
    font-weight: 200;
    font-size: 96px;
    fill: var(--soft-grey);
  }
  .quality-note {
    position: absolute;
    right: 100px;
    top: 1835px;
    margin: 0;
    text-align: right;
    font-family: "Raleway", sans-serif;
    font-weight: 300;
    font-size: 82px;
    line-height: 96px;
    color: var(--soft-grey);
  }
  .cable-length {
    position: absolute;
    left: 912px;
    top: 2080px;
    width: 200px;
    height: 112px;
    box-sizing: border-box;
    border: 3px solid var(--soft-grey);
    display: flex;
    align-items: center;
    justify-content: center;
    font-family: "Raleway", sans-serif;
    font-weight: 300;
    font-size: 96px;
    color: var(--soft-grey);
    line-height: 1;
  }
</style>
</head>
<body>
  <main class="package-front">
    <div class="package-frame"></div>

    <h1 class="brand-name">VELTOKA</h1>

    <svg class="artwork" viewBox="0 0 1200 2324" xmlns="http://www.w3.org/2000/svg">
      <defs>
        <linearGradient id="cable-tone" x1="0" y1="0" x2="0" y2="1">
          <stop offset="0" stop-color="var(--metal-light)"/>
          <stop offset="0.5" stop-color="var(--metal-mid)"/>
          <stop offset="1" stop-color="var(--cable-dark)"/>
        </linearGradient>
      </defs>

      <text class="headline-word" transform="translate(1020 1540) rotate(-90)" textLength="1160" lengthAdjust="spacingAndGlyphs">GUITAR</text>

      <text class="product-type" transform="translate(312 1460) rotate(-90)">instrument cable</text>

      <g role="img" aria-label="Product photo of a black guitar cable with two chrome jack plugs">
        <rect x="0" y="-40" width="1240" height="80" rx="30" fill="url(#cable-tone)" transform="translate(272 1792) rotate(-48)"/>
        <rect x="0" y="-40" width="620" height="80" rx="30" fill="url(#cable-tone)" transform="translate(712 1048) rotate(132)"/>
      </g>
    </svg>

    <p class="quality-note">High<br>Quality</p>
    <div class="cable-length">5m</div>
  </main>
</body>
</html>
```